Design einer Kundenbroschüre für Onlineplattform
Zielgruppe
Wir sind eine Onlineplattform, die den Einstieg in die Elektromobilität für Neuwagenkunden so einfach wie das Buchen einer Pauschalreise macht. Unser Kunden erhalten dafür ein individuell auf ihre Bedürfnisse abgestimmstes Gesamtpaket aus E-Auto, Ladelösung, Ökostrom und mehr.
In diesem Wettbewerb wollen wir von Euch eine Kundenbroschüre entwerfen lassen, die Kunden von Autohäusern zur Verfügung gestellt werden soll. Dabei steht im Vordergrund, dass der Prozess bzw. unsere Leistung einfach und verständlich ist.
Hintergrundwissen:
Im Gegensatz zu herkömmlichen Autokauf ist bei einem Kauf eines Elektroauto deutlich mehr zu beachten. So müssen nebem dem Auto noch weitere Komponenten beachtet werden. Im Detail handelt es sich dabei um fünf zusätzliche Komponenten:
1. Laden zu Hause: Eine geeignete Ladelösung zum Laden des E-Autos zu Hause zu finden und diese installieren lassen
2. Laden unterwegs: Eine passende Ladekarte für das Laden unterwegs (In- und Ausland) raussuchen.
3. Ökostrom/Autostrom: Einen günstigen und ökologischen Stromtarif finden
4. Digital Services & Apps: Anwendungen, die die Elektromobilität im Alltag vereinfachen
5. Umweltbonus : Unterstützung bei der Suche und Beantragung der Förderprämie (Umweltbonus) für Elektroautos
Wir übernehmen diese fünf Komponenten für die Kunden eines Autohauses und möchten diese im Vorfeld mit der Broschüre über unseren Service informieren.
Die Kunden sind dabei zwischen 30 und 60 Jahren, Neuwagenkäufer einer Premiummarke und beschäftigen sich mit dem Thema Elektromobilität vermutlich zum ersten Mal.
Aufgabenstellung
Es sollten folgende Themenfelder berücksichtigt sein:
1. Cover mit Logo und Bild ggf. weiteres Element
2. Über uns
3. Eine Übersicht wie der Prozess abläuft (Customer Journey).
4. Eine separate Übersicht über unsere Leistungen im allgemeinen
5. Eine separate Übersicht über unser spezielles Produkt.
Wir haben Euch im Anhang unseren ersten Entwurf angehängt. An diesen müsst ihr euch in keiner Weise halten, allerdings sollten sich die Texte auf den entsprechenden Seiten wiederfinden
Auf jeder Seite sollte in der Fußzeile unser Impressum (als Platzhalter einfügen bitte)
Bitte ausdrücklich nicht das Design unsere momentanen Website als Maßstab nehmen!
Schriftart: Open Sans
Farbcodes:
rosa/pink (HEX: #FF0083, RGB: (255,0,131), CMYK: (0, 100, 49,0))
grau: irgendeine RGBA Abstufung von Schwarz oder #4A4A4A

```html
<!DOCTYPE html>
<html lang="de">
<head>
<meta charset="utf-8">
<title>StromStart – Kundenbroschüre</title>
<link href="https://fonts.googleapis.com/css2?family=Open+Sans:wght@400;600;700;800&display=swap" rel="stylesheet">
<style>
:root{
  --pink:#e6318c;
  --purple:#4e4598;
  --text:#333333;
  --muted:#e4e4e4;
  --bg:#ffffff;
}
*{box-sizing:border-box;margin:0;padding:0}
html,body{width:778px;height:1200px;overflow:hidden;background:var(--bg)}
body{position:relative;font-family:"Open Sans",Arial,sans-serif;color:var(--text)}
.page{position:absolute;width:333px;height:470px;background:#fff;box-shadow:0 1px 4px rgba(0,0,0,.18);overflow:hidden}
.page > *{position:absolute}
.p1{left:41px;top:46px}.p2{left:405px;top:46px}.p3{left:42px;top:626px}.p4{left:405px;top:626px}
.page-label{position:absolute;width:333px;text-align:center;font-weight:800;font-size:25px;letter-spacing:1px;color:var(--muted)}

/* cover */
.cover-frame{inset:0;border:14px solid var(--purple)}
.brand-mark{font-weight:800;color:var(--purple);display:flex;align-items:center;gap:4px}
.brand-mark .dot{width:7px;height:7px;border-radius:50%;background:var(--pink)}
.cover-brand{left:0;right:0;top:98px;justify-content:center;font-size:22px}
.cover-blob{left:66px;top:144px}
.cover-title{left:66px;width:200px;top:196px;text-align:center;color:#fff}
.cover-title h1{font-size:26px;font-weight:700;line-height:1.15}
.cover-title p{font-size:11px;line-height:1.45;margin-top:5px}
.skyline{left:14px;right:14px;top:372px;height:84px;background:linear-gradient(180deg,#fff 0%,#ececec 100%)}

/* shared header / footer */
.head{left:24px;top:26px}
.head h2{font-size:11.5px;font-weight:700;color:var(--purple);line-height:1.2}
.head p{font-size:9px;color:var(--pink);line-height:1.3}
.corner-brand{right:18px;top:30px;font-size:10px}
.imprint{left:22px;top:437px;font-size:4.2px;line-height:1.35;color:#444}
.imprint b{font-weight:700}
.dealer{right:17px;top:444px;display:flex;align-items:center;gap:5px}
.dealer .badge{width:11px;height:11px;border-radius:50%;background:#555}
.dealer .badge.ring{background:#fff;border:1.3px solid #555}
.dealer span{font-size:5.2px;font-weight:700;line-height:1.1;color:#222;margin-left:2px}

/* page 2 */
.col{width:140px;font-size:5.3px;line-height:1.48}
.col h3{font-size:7px;font-weight:700;color:var(--purple);margin-bottom:5px}
.col b{font-weight:700}
.about{left:22px;top:78px}
.team{left:180px;top:78px}
.hero-photo{left:22px;top:201px;width:292px;height:116px;border-radius:8px;background:radial-gradient(circle at 75% 50%,#3a8a3e 0%,#1e4a22 30%,#2b2b2b 60%,#4a4038 100%)}
.how{left:22px;top:330px}
.how2{left:178px;top:341px}

/* page 3 journey */
.journey-line{left:0;top:0}
.step-icon{width:54px;height:54px;border-radius:50%;background:var(--pink);display:flex;align-items:center;justify-content:center}
.step-icon svg{width:32px;height:32px}
.step-card{width:74px;height:58px;background:#fff;border-radius:3px;box-shadow:0 1px 3px rgba(0,0,0,.15);text-align:center;padding-top:13px}
.step-card h4{font-size:6.6px;font-weight:700;color:var(--purple);line-height:1.25;margin-bottom:3px}
.step-card p{font-size:5.4px;line-height:1.45}
.total{width:50px;height:50px;border-radius:50%;background:var(--purple);color:#fff;font-size:6.4px;font-weight:700;text-align:center;line-height:1.35;display:flex;align-items:center;justify-content:center;border:2px solid #fff;box-shadow:0 0 0 1px var(--purple)}
.you{left:12px;top:86px;text-align:center;font-size:5.2px;font-weight:700}
.you i{display:block;width:20px;height:20px;border:1.3px solid #555;border-radius:50%;margin:0 auto 4px}

/* page 4 services */
.service{left:75px;width:243px;background:#fff;box-shadow:0 1px 4px rgba(0,0,0,.14);border-radius:2px;padding:9px 20px 0 21px}
.service h4{font-size:6.8px;font-weight:700;color:var(--purple);margin-bottom:4px}
.service p{font-size:5.3px;line-height:1.5}
.service-icon{left:22px;width:50px;height:50px;border-radius:50%;background:var(--pink);display:flex;align-items:center;justify-content:center}
.service-icon svg{width:30px;height:30px}
</style>
</head>
<body>

<svg width="0" height="0" style="position:absolute">
  <defs>
    <symbol id="i-car" viewBox="0 0 32 32"><g fill="none" stroke="#fff" stroke-width="1.4" stroke-linejoin="round"><path d="M4 21v-5l3-5h15l4 5 3 1v4z"/><circle cx="10" cy="22" r="2.5"/><circle cx="23" cy="22" r="2.5"/><path d="M13 15h4m0-2v4"/></g></symbol>
    <symbol id="i-pin" viewBox="0 0 32 32"><g fill="none" stroke="#fff" stroke-width="1.4"><path d="M10 20c-4-5-5-7-5-9a5 5 0 0 1 10 0c0 2-1 4-5 9z"/><circle cx="10" cy="11" r="2"/><path d="M22 22c-4-6-6-8-6-10a6 6 0 0 1 12 0c0 2-2 4-6 10z"/><circle cx="22" cy="12" r="2.3"/><path d="M10 20q0 6 8 6h4"/></g></symbol>
    <symbol id="i-doc" viewBox="0 0 32 32"><g fill="none" stroke="#fff" stroke-width="1.4"><rect x="7" y="5" width="15" height="21"/><path d="M10 10h9M10 14h9M10 18h5"/><path d="M17 24l10-10 2 2-10 10-3 1z"/></g></symbol>
    <symbol id="i-sign" viewBox="0 0 32 32"><g fill="none" stroke="#fff" stroke-width="1.4"><rect x="8" y="5" width="16" height="22" rx="1"/><path d="M11 11h10M11 15h10M11 19h6"/><path d="M18 23l2 2 4-5"/></g></symbol>
    <symbol id="i-station" viewBox="0 0 32 32"><g fill="none" stroke="#fff" stroke-width="1.4"><rect x="6" y="5" width="10" height="22"/><path d="M8 9h6M11 14l-2 4h3l-2 4"/><path d="M20 8v4m4-4v4m-6 0h8v3a4 4 0 0 1-8 0z"/><path d="M22 19v3a3 3 0 0 0 6 0v-2"/></g></symbol>
    <symbol id="i-bulb" viewBox="0 0 32 32"><g fill="none" stroke="#fff" stroke-width="1.4"><path d="M12 21c0-3-4-5-4-9a6 6 0 0 1 12 0c0 4-4 6-4 9z"/><path d="M12 24h4M13 27h2M14 2v2M5 6l2 2M23 6l-2 2M3 13h2M25 13h-2"/></g><path d="M22 26c0-5 3-8 8-8 0 5-3 8-8 8z" fill="#fff"/></symbol>
    <symbol id="i-screen" viewBox="0 0 32 32"><g fill="none" stroke="#fff" stroke-width="1.4"><rect x="4" y="6" width="24" height="16" rx="1"/><path d="M4 19h24M14 22v4M10 27h12"/><circle cx="16" cy="12.5" r="2"/><path d="M18 12.5v1a1.3 1.3 0 0 0 2.5 0v-1a4.5 4.5 0 1 0-2 3.7"/></g></symbol>
  </defs>
</svg>

<!-- Seite 1: Cover -->
<section class="page p1">
  <div class="cover-frame"></div>
  <div class="brand-mark cover-brand"><i class="dot"></i>StromStart</div>
  <svg class="cover-blob" width="200" height="200" viewBox="0 0 200 200" aria-hidden="true">
    <path d="M10 70c0-30 40-40 70-25l80-2c20 10 25 45 5 60l-90 60c-30 15-60 0-60-25z" fill="var(--purple)"/>
    <path d="M95 5c25-5 35 20 50 50 12 25 40 70 50 95 8 25-25 45-55 30-35-20-70-15-105-30-35-15-40-40-25-65 20-25 40-70 85-80z" fill="var(--pink)" stroke="#fff" stroke-width="1.5"/>
  </svg>
  <div class="cover-title"><h1>Strom<br>Start</h1><p>Dein Partner für die<br>E-Mobilität</p></div>
  <div class="skyline" role="img" aria-label="Gezeichnete Stadtsilhouette mit Türmen, Bergen, Windrädern, Bäumen und Elektroauto"></div>
</section>
<div class="page-label" style="left:41px;top:540px">SEITE 1</div>

<!-- Seite 2: Über uns -->
<section class="page p2">
  <div class="head"><h2>StromStart</h2><p>Dein Partner für E-Mobilität</p></div>
  <div class="brand-mark corner-brand"><i class="dot"></i>StromStart</div>
  <div class="col about">
    <h3>Über uns</h3>
    <p><b>StromStart</b> ist eine Online-Plattform, die Ihnen den <b>Einstieg in die Elektromobilität</b> erleichtert. Wir bieten unseren Kunden ein individuell auf Ihre Bedürfnisse abgestimmtes <b>Gesamtpaket aus E-Auto, Ladelösung, Ökostrom und mehr.</b><br>Sie können den Service ganz einfach von Zuhause nutzen und bekommen alle nötigen Informationen online zugesendet. Zudem haben Sie immer die Möglichkeit sich <b>Kostenfrei</b> telefonisch bei unseren Kundenservice zu melden.</p>
  </div>
  <div class="col team">
    <h3>Wer wir sind</h3>
    <p><b>StromStart</b> ist ein Team aus leidenschaftlichen Ingenieuren, Machine-Learning Profis, Finanzexperten, Social Media Gurus, Stromnetzverstehern und Rechtswissenschaftlern, die sich für die Zukunft unserer Mobilität begeistern!<br>Unser Ziel ist es, den <b>Einstieg in die Elektromobilität einfach und zeitsparend zu gestalten.</b> Wir helfen Ihnen, das richtige Gesamtpaket zu finden und kümmern uns um die Details wie <b>Terminvereinbarungen &amp; Koordination von Handwerkern.</b></p>
  </div>
  <div class="hero-photo" role="img" aria-label="Foto: Finger drückt einen grün leuchtenden Startknopf für E-Mobilität"></div>
  <div class="col how">
    <h3>Wie funktionierts</h3>
    <p>Ihr persönlicher Kundenberater des <b>Autohauses Berghof + Sommer</b> hat Ihnen einen personalisierten Link zur Verfügung gestellt, der Sie ebenso wie der QR-Code auf der letzten Seite zu unserem <b>Online-Assistenten</b> führt.<br>Sie starten den Assistenten und beantworten ein paar <b>Fragen</b>. Unser Team analysiert auf Basis Ihrer</p>
  </div>
  <div class="col how2">
    <p>Antworten <b>Ihre Bedürfnisse</b> und bespricht mit Ihnen die <b>Details des rund-um-sorglos Gesamtpakets.</b> Im Anschluss kümmert sich das Team von <b>StromStart</b> um die Organisation und Koordination der Handwerkertermine.<br>Die <b>Installation</b> Ihrer neuen Elektrolösung erfolgt innerhalb weniger Wochen.</p>
  </div>
  <p class="imprint"><b>StromStart Mobility GmbH</b><br>Sitz der Gesellschaft: Lindenau, Deutschland<br>Registergericht: AG Lindenau, HRB 100200<br>Geschäftsführer: Jonas Brehm, Lukas Brehm, Timo Kessler</p>
  <div class="dealer"><i class="badge ring"></i><i class="badge"></i><span>Berghof +<br>Sommer</span></div>
</section>
<div class="page-label" style="left:405px;top:540px">SEITE 2</div>

<!-- Seite 3: Customer Journey -->
<section class="page p3">
  <div class="head"><h2>Customer Journey</h2><p>Unser Service von E-Auto bis Umweltbonus</p></div>
  <div class="brand-mark corner-brand"><i class="dot"></i>StromStart</div>
  <svg class="journey-line" width="333" height="470" aria-hidden="true">
    <path d="M40 99H296a15 15 0 0 1 15 15V206a15 15 0 0 1-15 15H40a15 15 0 0 0-15 15V327a15 15 0 0 0 15 15H240" fill="none" stroke="var(--purple)" stroke-width="3"/>
    <g fill="var(--pink)">
      <path d="M119 93l6 6-6 6z"/><path d="M208 93l6 6-6 6z"/>
      <path d="M305 156h12l-6 7z"/>
      <path d="M214 215l-6 6 6 6z"/><path d="M125 215l-6 6 6 6z"/>
      <path d="M19 278h12l-6 7z"/>
      <path d="M119 336l6 6-6 6z"/><path d="M208 336l6 6-6 6z"/>
    </g>
  </svg>
  <div class="you"><i></i>Sie</div>

  <div class="step-icon" style="left:51px;top:72px"><svg><use href="#i-car"/></svg></div>
  <div class="step-card" style="left:41px;top:120px"><h4>1. E-Auto</h4><p>Wahl des<br>passenden<br>E-Autos</p></div>
  <div class="step-icon" style="left:140px;top:72px"><svg><use href="#i-pin"/></svg></div>
  <div class="step-card" style="left:130px;top:120px"><h4>2. Probefahrt</h4><p>Das gewählte<br>E-Auto probefah-<br>ren und testen</p></div>
  <div class="step-icon" style="left:230px;top:72px"><svg><use href="#i-sign"/></svg></div>
  <div class="step-card" style="left:220px;top:120px;padding-top:10px"><h4>3. Kauf und<br>Anmeldung</h4><p>Kauf des E-Autos<br>und Übergabe der<br>Dokumente</p></div>

  <div class="step-icon" style="left:51px;top:194px"><svg><use href="#i-bulb"/></svg></div>
  <div class="step-card" style="left:41px;top:242px"><h4>6. Autostrom</h4><p>Ermittlung passender Autostromtarife zum nachhaltigen Laden des E-Autos zu Hause.</p></div>
  <div class="step-icon" style="left:140px;top:194px"><svg><use href="#i-station"/></svg></div>
  <div class="step-card" style="left:130px;top:242px"><h4>5. Laden unterwegs</h4><p>Vermittlung bedarfs-<br>gerechter Ladekarten für öffentliche Ladesäulen</p></div>
  <div class="step-icon" style="left:230px;top:194px"><svg><use href="#i-car"/></svg></div>
  <div class="step-card" style="left:220px;top:242px"><h4>4. Ladelösung</h4><p>Vereinbarung einer Standortanalyse und Beratung &amp; Einbau der Wallboxen</p></div>

  <div class="step-icon" style="left:51px;top:315px"><svg><use href="#i-screen"/></svg></div>
  <div class="step-card" style="left:41px;top:363px"><h4>7. Digital Services</h4><p>Beratung zu digitalen Services, die die E-Mobilität im Alltag vereinfachen</p></div>
  <div class="step-icon" style="left:140px;top:315px"><svg><use href="#i-doc"/></svg></div>
  <div class="step-card" style="left:130px;top:363px"><h4>8. Umweltbonus</h4><p>Unterstützung bei<br>der Suche &amp;<br>Beantragung geeigneter Förderprämien</p></div>
  <div class="total" style="left:232px;top:317px">Ihr<br>Gesamt-<br>paket</div>

  <p class="imprint"><b>StromStart Mobility GmbH</b><br>Sitz der Gesellschaft: Lindenau, Deutschland<br>Registergericht: AG Lindenau, HRB 100200<br>Geschäftsführer: Jonas Brehm, Lukas Brehm, Timo Kessler</p>
  <div class="dealer"><i class="badge ring"></i><i class="badge"></i><span>Berghof +<br>Sommer</span></div>
</section>
<div class="page-label" style="left:42px;top:1122px">SEITE 3</div>

<!-- Seite 4: Serviceangebot -->
<section class="page p4">
  <div class="head"><h2>Unser Serviceangebot im Detail</h2><p>Alles für den sorgenfreien Einstieg in die Elektromobilität</p></div>
  <div class="brand-mark corner-brand"><i class="dot"></i>StromStart</div>

  <div class="service" style="top:86px;height:54px"><h4>Wallbox – Zuhause laden</h4><p>Wir evaluieren, ob für Sie zuhause eine Wallbox infrage kommt oder ob Sie auf öffentliche Lademöglichkeiten zugreifen können. Ferner organisieren wir die Standortanalyse Vorort sowie deren Einbau und Anschluss.</p></div>
  <div class="service-icon" style="top:88px"><svg><use href="#i-car"/></svg></div>

  <div class="service" style="top:148px;height:53px"><h4>Autostrom</h4><p>Wir ermitteln geeignete Autostrom-Tarife und leiten bei Bedarf den hierfür benötigten Einbau eines separaten Zählers durch den Stromversorger in die Wege. Auch bei der Integration von Solaranlagen oder Wandbatterien stehen wir Ihnen beratend zur Seite.</p></div>
  <div class="service-icon" style="top:152px"><svg><use href="#i-bulb"/></svg></div>

  <div class="service" style="top:215px;height:54px"><h4>Ladekarten- Laden unterwegs</h4><p>Damit Sie auch unterwegs und im Ausland an öffentlichen Ladesäulen Ihr E-Auto überall laden können, finden wir abgestimmt auf die jeweiligen Nutzungsverhalten und Bedürfnisse die passenden Ladekarten.</p></div>
  <div class="service-icon" style="top:217px"><svg><use href="#i-station"/></svg></div>

  <div class="service" style="top:280px;height:54px"><h4>Digital Services &amp; Apps</h4><p>Zusätzlich schnüren wir für unsere Kunden ein Paket aus nützlichen Apps zum Thema Elektromobilität, die ie bequem über ihr Smartphone nutzen können.</p></div>
  <div class="service-icon" style="top:282px"><svg><use href="#i-screen"/></svg></div>

  <div class="service" style="top:344px;height:54px;padding-top:14px"><h4>Umweltprämie</h4><p>Wir suchen für Sie geeignete Förderprogramme heraus und unterstützen Sie bei Beantragung der Fördermittel.</p></div>
  <div class="service-icon" style="top:345px"><svg><use href="#i-doc"/></svg></div>

  <p class="imprint"><b>StromStart Mobility GmbH</b><br>Sitz der Gesellschaft: Lindenau, Deutschland<br>Registergericht: AG Lindenau, HRB 100200<br>Geschäftsführer: Jonas Brehm, Lukas Brehm, Timo Kessler</p>
  <div class="dealer"><i class="badge ring"></i><i class="badge"></i><span>Berghof +<br>Sommer</span></div>
</section>
<div class="page-label" style="left:405px;top:1122px">SEITE 4</div>

</body>
</html>
```